Newly opened kids play space needs brochure to show what our space has to offer

Tri-fold color brochure with same aethetic as website (www.fernhollowplayhouse.com) that provides a comprehensive and visual overview of what our play space is comprised of. Features of the brochure should include our logo, "A Steiner and Reggio-inspired Play Space in the Poconos", photos of: Dedicated Infant Play Area; Cafe and Free WiFi; Weekly Themed Activities; Unique Classes; Parties and Events. Photos also of our open play area with children playing within it. Info within the brochure should include our location, hours. Please take some copy from : https://www.facebook.com/fernhollowkinderplayhouse/?ref=bookmarks
and from the Plan Your Visit part of the website. I have a lot of photos to use; is there a way to put in generic photo placeholders and I can pick which photos of mine to go into the various areas of the brochure, or if you need the photos ahead of time, please let me know the best way to proceed. I am attaching the logo files for now.

Font styles to use
Sans Serif

Colors
85cae6
cee9f5
86cfc6
cfeae6
fdf9cf
fff3d1
eaf2ce
cadf82

Requirements
Must have
• Eye catching placement of photos; color scheme similar to website and logo colors
Should not have
• Brochure should be simple, not too colorful - no primary colors, not too crowded.

```html
<!DOCTYPE html>
<html lang="en">
<head>
<meta charset="utf-8">
<title>Fern Hollow Tri-fold Brochure</title>
<link rel="stylesheet" href="https://fonts.googleapis.com/css2?family=Open+Sans:wght@300;400;600;700&family=Ubuntu:wght@500;700&display=swap">
<style>
:root{
  --stage:#a9a9a9;
  --cream:#ece8d8;
  --stone:#dcd8c7;
  --green:#4f9a6c;
  --green-light:#76b59a;
  --red:#b5433f;
  --red-deep:#9e3a36;
  --blue-top:#2b9ccb;
  --blue-bottom:#1a5e93;
  --lime:#8cbf4b;
  --sky:#84c5e2;
  --sky-deep:#6fb3d5;
  --teal:#68b4aa;
  --ocean:#3e88b0;
  --ink-blue:#1f7fae;
  --ink-brown:#4a2a22;
  --photo-warm:#a7826a;
  --photo-cool:#8b8f93;
}
*{box-sizing:border-box;margin:0;padding:0}
html,body{width:916px;height:1200px;overflow:hidden;background:var(--stage)}
body{position:relative;font-family:"Open Sans",sans-serif;color:var(--ink-brown)}
.brochure{position:absolute;left:98px;width:720px;height:540px;display:flex;box-shadow:0 18px 30px rgba(0,0,0,.25)}
.brochure--outside{top:30px}
.brochure--inside{top:630px}
.panel{position:relative;width:240px;height:540px;overflow:hidden;background:var(--cream)}
.panel + .panel{border-left:1px solid rgba(0,0,0,.08)}
.panel-shapes{position:absolute;inset:0;width:240px;height:540px}
.abs{position:absolute;left:0;right:0;text-align:center}

/* visit panel */
.visit-title{top:40px;font-weight:300;font-size:17px;color:#fff;letter-spacing:.3px}
.visit-copy{top:74px;padding:0 26px;font-size:9px;line-height:1.35;color:#fff;font-weight:600}
.pill{position:absolute;left:38px;width:164px;height:30px;border-radius:8px;background:var(--red);color:#fff;font-size:11.5px;display:flex;align-items:center;justify-content:center}
.pill--admission{top:232px;box-shadow:0 0 0 2px #fff inset,0 0 0 3px var(--red)}
.pill--member{top:282px;background:var(--red-deep)}
.pill-or{top:266px;font-size:8px;color:#555}
.hours{position:absolute;left:40px;top:336px;width:160px;height:150px;border:1px solid #8a6a5c;background:#f4f1e6;text-align:center;padding-top:12px}
.hours h3{font-size:11.5px;font-weight:700;color:#2d1a14;margin-top:4px}
.hours .days{font-size:8px;color:var(--red);font-weight:600}
.hours .time{font-size:8px;color:#333;margin-bottom:6px}

/* contact panel */
.panel--contact{background:linear-gradient(160deg,var(--blue-top),var(--blue-bottom))}
.intro{top:44px;padding:0 30px;color:#fff;font-size:19px;line-height:1.6;font-weight:400}
.icon-dot{position:absolute;left:102px;width:36px;height:36px;border-radius:50%;background:var(--lime);display:flex;align-items:center;justify-content:center}
.icon-dot--phone{top:290px}
.icon-dot--pin{top:370px}
.contact-line{color:#fff;font-size:10px;font-weight:600;line-height:1.3}
.contact-phone{top:336px}
.contact-address{top:416px}
.web-pill{position:absolute;left:22px;top:480px;width:196px;height:26px;border-radius:13px;background:var(--lime);color:#fff;font-size:10.5px;font-weight:600;display:flex;align-items:center;justify-content:center}

/* cover panel */
.brand{top:302px;font-family:"Ubuntu",sans-serif;font-weight:700;font-size:28px;color:var(--ink-blue);display:flex;align-items:center;justify-content:center;gap:8px}
.brand-dot{width:12px;height:12px;border-radius:50%;background:var(--lime)}
.brand-sub{top:342px;font-size:9px;color:var(--ink-blue);font-weight:600}
.slogan{top:395px;left:34px;right:20px;text-align:left;font-family:"Ubuntu",sans-serif;font-weight:700;font-size:26px;line-height:1.35;color:var(--ink-blue)}

/* inside panels */
.feature-title{top:52px;font-family:"Ubuntu",sans-serif;font-weight:700;font-size:21px;line-height:1.2;color:var(--ink-brown)}
.feature-icon{position:absolute;left:96px;top:148px;width:48px;height:48px;border-radius:50%;background:var(--sky-deep);border:3px solid #fff;display:flex;align-items:center;justify-content:center}
.feature-copy{padding:0 24px;font-size:11px;font-weight:700;line-height:1.35;color:var(--ink-brown)}
.feature-copy--top{top:226px}
.feature-copy--bottom{top:452px}
.photo{position:absolute;left:20px;width:200px;border-bottom:4px solid #2a83c9}
.photo--cafe{top:318px;height:190px;background:linear-gradient(135deg,var(--photo-warm),#5c4a42)}
.photo--infant{top:190px;height:190px;background:linear-gradient(135deg,#b99a84,#3f3a3e)}
.photo--themed{top:286px;height:200px;background:linear-gradient(135deg,var(--photo-cool),#4b4a40)}
</style>
</head>
<body>

<section class="brochure brochure--outside">
  <article class="panel panel--visit">
    <svg class="panel-shapes" viewBox="0 0 240 540">
      <path d="M0 0H240V150L0 200Z" fill="var(--green)"/>
      <path d="M0 200L240 150V160L0 214Z" fill="var(--green-light)"/>
    </svg>
    <h2 class="abs visit-title">PLAN YOUR VISIT!</h2>
    <p class="abs visit-copy">Fern Hollow offers open-ended, natural toys and activities that nurture the child's sense of wonder and invites them to explore in our serene and spacious environment.</p>
    <div class="pill pill--admission">$12 Daily Admission</div>
    <div class="abs pill-or">or</div>
    <div class="pill pill--member">Become a Member</div>
    <div class="hours">
      <h3>Open Play</h3>
      <div class="days">Mon, Wed, Fri, Sun</div>
      <div class="time">10:00AM - 5:00PM</div>
      <div class="days">Tue, Thu, Sat</div>
      <div class="time">10:00AM - 7:00PM</div>
      <h3>Infants Only</h3>
      <div class="days">Monday through Friday</div>
      <div class="time">9:00AM - 10:00AM</div>
    </div>
  </article>

  <article class="panel panel--contact">
    <p class="abs intro">We are a forest and meadow-inspired play space located in the Poconos.</p>
    <div class="icon-dot icon-dot--phone">
      <svg width="18" height="18" viewBox="0 0 24 24"><path d="M6.6 10.8a15 15 0 0 0 6.6 6.6l2.2-2.2c.3-.3.7-.4 1-.2 1.1.4 2.3.6 3.6.6.6 0 1 .4 1 1V20c0 .6-.4 1-1 1A17 17 0 0 1 3 4c0-.6.4-1 1-1h3.5c.6 0 1 .4 1 1 0 1.3.2 2.5.6 3.6.1.3 0 .7-.2 1Z" fill="var(--blue-bottom)"/></svg>
    </div>
    <p class="abs contact-line contact-phone">(272) 555-0148</p>
    <div class="icon-dot icon-dot--pin">
      <svg width="18" height="18" viewBox="0 0 24 24"><path d="M12 2a7 7 0 0 0-7 7c0 5.3 7 13 7 13s7-7.7 7-13a7 7 0 0 0-7-7Zm0 9.5A2.5 2.5 0 1 1 12 6.5a2.5 2.5 0 0 1 0 5Z" fill="var(--blue-bottom)"/></svg>
    </div>
    <p class="abs contact-line contact-address">48 Laurel Bend Road,<br>Alder Springs, AS 10482</p>
    <div class="web-pill">www.fernhollowplayhouse.com</div>
  </article>

  <article class="panel panel--cover">
    <svg class="panel-shapes" viewBox="0 0 240 540">
      <defs>
        <linearGradient id="coverPhoto" x1="0" y1="0" x2="1" y2="1">
          <stop offset="0" stop-color="#b08a6c"/>
          <stop offset="1" stop-color="#6a5448"/>
        </linearGradient>
      </defs>
      <path d="M0 0H240V250L0 205Z" fill="url(#coverPhoto)" role="img" aria-label="Photo: child smiling on the play room floor"/>
      <path d="M0 205L240 250V275L0 215Z" fill="var(--sky)"/>
    </svg>
    <div class="abs brand"><span class="brand-dot"></span>Fern Hollow</div>
    <p class="abs brand-sub">A Kinder Play Space</p>
    <p class="abs slogan">Play. Learn.<br>Grow.</p>
  </article>
</section>

<section class="brochure brochure--inside">
  <article class="panel panel--cafe" style="background:var(--cream)">
    <svg class="panel-shapes" viewBox="0 0 240 540">
      <path d="M0 0H240V168L0 140Z" fill="var(--sky)"/>
      <path d="M0 143L240 171" stroke="#fff" stroke-width="3"/>
      <path d="M0 149L240 177" stroke="var(--sky-deep)" stroke-width="1"/>
    </svg>
    <h2 class="abs feature-title">Cafe and WIFI</h2>
    <div class="feature-icon">
      <svg width="24" height="24" viewBox="0 0 24 24"><path d="M4 6h13v6a5 5 0 0 1-5 5H9a5 5 0 0 1-5-5Zm13 2h2a2 2 0 0 1 0 4h-2M3 20h16" fill="none" stroke="#fff" stroke-width="2"/></svg>
    </div>
    <p class="abs feature-copy feature-copy--top">Take a break or catch up on work while enjoying Kettleworth coffee, beverages, and healthy snacks.</p>
    <div class="photo photo--cafe" role="img" aria-label="Photo: parent enjoying coffee at a cafe table"></div>
  </article>

  <article class="panel panel--infant" style="background:var(--stone)">
    <svg class="panel-shapes" viewBox="0 0 240 540">
      <path d="M0 0H240V140L0 148Z" fill="var(--teal)"/>
      <path d="M0 150L240 142" stroke="#fff" stroke-width="3"/>
    </svg>
    <h2 class="abs feature-title">Dedicated<br>Infant Area</h2>
    <div class="feature-icon" style="top:124px">
      <svg width="24" height="24" viewBox="0 0 24 24"><circle cx="12" cy="7" r="3" fill="#fff"/><path d="M6 20c0-5 2.7-8 6-8s6 3 6 8Z" fill="#fff"/></svg>
    </div>
    <div class="photo photo--infant" role="img" aria-label="Photo: parent and baby at a wooden play gym"></div>
    <p class="abs feature-copy feature-copy--bottom">Bond safely with your baby while being within eyeshot of the main play area.</p>
  </article>

  <article class="panel panel--themed" style="background:var(--stone)">
    <svg class="panel-shapes" viewBox="0 0 240 540">
      <path d="M0 0H240V130L0 158Z" fill="var(--ocean)"/>
      <path d="M0 160L240 132" stroke="#fff" stroke-width="3"/>
    </svg>
    <h2 class="abs feature-title" style="top:44px">Themed<br>Activities</h2>
    <div class="feature-icon" style="top:122px">
      <svg width="24" height="24" viewBox="0 0 24 24"><path d="M12 3l2.6 5.6 6 .7-4.5 4.1 1.2 6L12 16.4 6.7 19.4l1.2-6L3.4 9.3l6-.7Z" fill="#fff"/></svg>
    </div>
    <p class="abs feature-copy" style="top:190px">Stories, crafts, and activities change weekly to celebrate the seasons and the world around us.</p>
    <div class="photo photo--themed" role="img" aria-label="Photo: families potting flowers together on the floor"></div>
  </article>
</section>

</body>
</html>
```